Small Ecommerce Styled Site to Sell / Lease Domain Names

We have a small portfolio of 100+ domain names that we would like to offer for sale or lease via a web site. Along the lines of http://www.velramarkets.com/searchdomain.html?priceChoice=2&sort=leasing_desc

We would like initially a 4 page design, listing page (as site referenced above), domain info page (Universal Domain Name Landing Page with form) and checkout a page and About Us Page

We do not want a replica of the site listed, please use it as a guide only, we are looking for a fresh design, in similar concept web 2.0

Our Colours are #351a41 (Main) - #ffca27 (Secondary) all other colours must compliment those 2.
Updates

Domain Landing Page:  I am sorry I was not clear about expectations, however we would like a domain landing page that would be the default holding page for a domain name.

For some examples of what I mean please see:
https://www.pobexhub.com.au/guest-articles/7626-domain-for-sale-landing-pages.html
http://dev.quillterbrokers.com/blog/2013/09/sales-only-landers-and-buy-it-now-2/

Industry/Entity Type

Domain

Font styles to use
Sans Serif

```html
<!DOCTYPE html>
<html lang="en">
<head>
<meta charset="utf-8">
<title>Parcelnest – Buy Domains</title>
<link rel="stylesheet" href="https://fonts.googleapis.com/css2?family=Arimo:wght@400;700&family=Tinos:ital@1&display=swap">
<style>
:root{
  --main:#351a41;
  --main-dark:#25112e;
  --accent:#ffca27;
  --accent-dark:#e9ac12;
  --nav-text:#4a2a4f;
  --text:#555;
  --line:#dddddd;
  --row-bg:#f6f6f6;
  --btn:#5a5f66;
  --footer:#4b4b4b;
  --footer-bottom:#3c3c3c;
  --footer-link:#b4b4b4;
}
*{box-sizing:border-box;margin:0;padding:0}
html,body{width:900px;height:1200px;overflow:hidden}
body{position:relative;background:#fff;font-family:"Arimo",Arial,sans-serif;color:var(--text)}
.abs{position:absolute}

/* top bar */
.topbar{left:0;top:0;width:900px;height:28px;background:var(--main-dark);color:#fff;font-size:8px}
.topbar .call{left:132px;top:9px;display:flex;align-items:center;gap:5px}
.topbar .links{right:131px;top:9px;display:flex;gap:14px}
.topbar .links span{display:flex;align-items:center;gap:4px}

/* header */
.header{left:0;top:28px;width:900px;height:106px;background:linear-gradient(#3d1f4a,var(--main))}
.brand{left:130px;top:17px;font-size:23px;font-weight:700;color:var(--accent);letter-spacing:-.5px}
.follow{left:613px;top:30px;display:flex;align-items:center;gap:5px;color:#fff;font-size:8px}
.follow .soc{width:25px;height:25px;border-radius:50%;border:1.5px solid #fff}

/* nav */
.nav{left:129px;top:101px;width:642px;height:33px;background:#fff;display:flex}
.nav a{text-decoration:none;color:var(--nav-text);font-size:10px;display:flex;align-items:center;justify-content:center;height:100%}
.nav a.active{background:linear-gradient(#ffd447,#f3b61c);width:122px}

/* search */
.search-label{left:153px;top:157px;font-family:"Tinos",Georgia,serif;font-style:italic;font-size:14px;color:var(--main)}
.search-input{left:289px;top:152px;width:377px;height:28px;border:1px solid #ccc;border-radius:3px;display:flex;align-items:center;padding-left:9px;gap:7px;font-size:9px;color:#777}
.search-btn{left:676px;top:153px;width:86px;height:26px;border-radius:3px;background:linear-gradient(#ffd447,#f1b11a);border:1px solid var(--accent-dark);color:#6a4a12;font-size:11px;display:flex;align-items:center;justify-content:center}
.adv{left:289px;top:190px;font-size:8px;font-style:italic;color:#e0a210;text-decoration:underline}
.divider{left:128px;top:213px;width:643px;height:1px;background:linear-gradient(90deg,transparent,#ddd 15%,#ddd 85%,transparent)}

/* filter tabs */
.filters{left:128px;top:231px;display:flex;gap:9px}
.filter{width:100px;height:35px;border:1px solid #d6d6d6;border-radius:3px;background:linear-gradient(#fafafa,#ececec);display:flex;align-items:center;padding-left:8px;gap:5px;font-size:8.5px;color:#333;position:relative;white-space:nowrap}
.filter .chev{position:absolute;right:6px;top:11px;width:12px;height:12px;border-radius:50%;border:1px solid #aaa}
.filter .chev::after{content:"";position:absolute;left:3px;top:2px;width:4px;height:4px;border-right:1px solid #888;border-bottom:1px solid #888;transform:rotate(45deg)}

/* listing panel */
.listing{left:128px;top:319px;width:643px;height:575px;border:1px solid #e2e2e2;background:#fff}
.listing .bar{height:50px;background:linear-gradient(#fff,#efefef)}
.table{left:140px;top:378px;width:622px;border-collapse:collapse;font-size:9px}
.table th{height:29px;background:var(--main);color:#fff;font-weight:400;text-align:left;padding-left:14px}
.table td{height:29.9px;background:var(--row-bg);border:1px solid #e0e0e0;color:#555}
.table td.name{width:214px;padding-left:15px}
.table td.cat{width:174px;padding-left:13px}
.table td.cat span{display:flex;align-items:center;gap:5px}
.table td.price{width:115px;text-align:center}
.table td.act{text-align:center}
.pill{display:inline-block;width:72px;height:17px;line-height:17px;border-radius:2px;background:linear-gradient(#ffd447,#f1b11a);border:1px solid var(--accent-dark);color:#5a3e0a;font-size:8.5px}
.offer{display:inline-block;width:73px;height:19px;line-height:19px;border-radius:2px;background:linear-gradient(#6a7078,var(--btn));color:#fff;font-size:8.5px}
.ico{width:10px;height:10px;flex:none}

/* dropdown */
.dropdown{left:128px;top:271px;width:521px;height:144px;background:#fff;border:1px solid #dcdcdc;box-shadow:0 2px 5px rgba(0,0,0,.12)}
.dd-col{top:14px;width:140px;font-size:8px;color:#555}
.dd-item{height:23.7px;display:flex;align-items:center;gap:6px;border-bottom:1px solid #ddd}
.dd-item.last{border-bottom:none}
.plus{width:8px;height:8px;border:1px solid #aaa;position:relative;flex:none}
.plus::before{content:"";position:absolute;left:1px;top:2.5px;width:4px;height:1px;background:#777}
.plus::after{content:"";position:absolute;left:2.5px;top:1px;width:1px;height:4px;background:#777}

/* pagination */
.pager{left:474px;top:905px;display:flex;gap:7.4px}
.pager span{height:18px;min-width:18px;border:1px solid #d8d8d8;border-radius:2px;background:#fff;font-size:9px;font-weight:700;color:#333;display:flex;align-items:center;justify-content:center}
.pager .wide{width:39px}

/* footer */
.footer{left:0;top:956px;width:900px;height:211px;background:var(--footer)}
.fcol{top:22px;font-size:7.8px;color:var(--footer-link)}
.fcol h3{font-size:11px;font-weight:400;color:#fff;margin-bottom:6px}
.fcol li{list-style:none;height:15.5px}
.verified{left:540px;top:154px;width:80px;height:34px;border-radius:3px;background:#6a6a6a}
.cards{left:632px;top:162px;display:flex;gap:4px}
.cards span{width:31px;height:17px;border-radius:2px;background:#fff}
.copyright{left:0;top:1167px;width:900px;height:33px;background:var(--footer-bottom);color:#aaa;font-size:7.8px;display:flex;align-items:center;justify-content:center}
</style>
</head>
<body>
<svg width="0" height="0" style="position:absolute">
  <symbol id="i-cart" viewBox="0 0 10 10"><path d="M0 1h2l1.5 5h5L10 2.5H3" fill="none" stroke="#333" stroke-width="1"/><circle cx="4" cy="8.3" r=".9" fill="#333"/><circle cx="8" cy="8.3" r=".9" fill="#333"/></symbol>
  <symbol id="i-pin" viewBox="0 0 10 10"><path d="M5 9.5C2.5 6.5 2 5 2 4a3 3 0 0 1 6 0c0 1-.5 2.5-3 5.5z" fill="none" stroke="#333"/><circle cx="5" cy="4" r="1" fill="#333"/></symbol>
  <symbol id="i-key" viewBox="0 0 10 10"><circle cx="6.5" cy="3.5" r="2.3" fill="none" stroke="#333"/><path d="M5 5L1 9" stroke="#333" stroke-width="1.2"/></symbol>
  <symbol id="i-bank" viewBox="0 0 10 10"><path d="M1 3.5L5 1l4 2.5z" fill="#333"/><path d="M2 4.5v3.5M4 4.5v3.5M6 4.5v3.5M8 4.5v3.5" stroke="#333"/><path d="M1 9h8" stroke="#333" stroke-width="1.2"/></symbol>
  <symbol id="i-rocket" viewBox="0 0 10 10"><path d="M9 1C6 1 3.5 3 2.5 6l1.5 1.5C7 6.5 9 4 9 1z" fill="none" stroke="#333"/><path d="M2.5 6L1 9l3-1.5" fill="none" stroke="#333"/></symbol>
  <symbol id="i-cap" viewBox="0 0 10 10"><path d="M0.5 3.5L5 1.5l4.5 2L5 5.5z" fill="none" stroke="#333"/><path d="M2.5 4.5v2.5c1.5 1.2 3.5 1.2 5 0V4.5" fill="none" stroke="#333"/></symbol>
</svg>

<div class="abs topbar">
  <div class="abs call"><svg width="9" height="9" viewBox="0 0 10 10"><path d="M2 1l2 2-1 1.2c.6 1.3 1.5 2.2 2.8 2.8L7 6l2 2-1.5 1.5C4 9 1 6 .5 2.5z" fill="#9b7aa8"/></svg>Call us : (1045)118 306</div>
  <div class="abs links">
    <span><svg width="8" height="8" viewBox="0 0 10 10"><circle cx="5" cy="3" r="2.3" fill="#9b7aa8"/><path d="M1 10c0-3 2-4.5 4-4.5S9 7 9 10z" fill="#9b7aa8"/></svg>Signup</span>
    <span><svg width="8" height="8" viewBox="0 0 10 10"><rect x="1.5" y="4.5" width="7" height="5" fill="#9b7aa8"/><path d="M3 4.5V3a2 2 0 0 1 4 0v1.5" fill="none" stroke="#9b7aa8"/></svg>Login</span>
    <span><svg width="9" height="8" viewBox="0 0 10 10"><path d="M0 1h2l1.5 5h5L10 2.5H3" fill="none" stroke="#9b7aa8" stroke-width="1.3"/><circle cx="4" cy="8.3" r="1" fill="#9b7aa8"/><circle cx="8" cy="8.3" r="1" fill="#9b7aa8"/></svg>Cart</span>
    <span><b style="color:#9b7aa8;font-weight:400">?</b>FAQ</span>
  </div>
</div>

<div class="abs header">
  <div class="abs brand">Parcelnest</div>
  <div class="abs follow">Follow Us :
    <div class="soc"></div><div class="soc"></div><div class="soc"></div><div class="soc"></div>
  </div>
</div>

<nav class="abs nav">
  <a class="active" href="#">Buy Domains</a>
  <a href="#" style="width:120px">Lease Domains</a>
  <a href="#" style="width:108px">Categories</a>
  <a href="#" style="width:92px">Valuation</a>
  <a href="#" style="width:96px">Affiliate</a>
  <a href="#" style="width:104px">Contact Us</a>
</nav>

<div class="abs search-label">Search by Categories :</div>
<div class="abs search-input"><svg width="11" height="11" viewBox="0 0 12 12"><circle cx="5" cy="5" r="3.8" fill="none" stroke="#999" stroke-width="1.3"/><path d="M8 8l3 3" stroke="#999" stroke-width="1.5"/></svg>Enter your Keywords</div>
<div class="abs search-btn">Search</div>
<div class="abs adv">Advanced search :</div>
<div class="abs divider"></div>

<div class="abs filters">
  <div class="filter"><svg width="13" height="15" viewBox="0 0 13 15"><rect x="1" y="1.5" width="11" height="13" rx="1" fill="none" stroke="#888"/><path d="M3 5h7M3 8h7M3 11h7" stroke="#888"/></svg>Categories<span class="chev"></span></div>
  <div class="filter"><svg width="13" height="11" viewBox="0 0 13 11"><path d="M1 1h11v9H1z M3 1v9M10 1v9" fill="none" stroke="#888"/></svg>Extensions<span class="chev"></span></div>
  <div class="filter"><svg width="12" height="11" viewBox="0 0 13 11"><path d="M1 10h2V7H1zM4 10h2V5H4zM7 10h2V3H7zM10 10h2V1h-2z" fill="#999"/></svg>Price Range<span class="chev"></span></div>
  <div class="filter"><svg width="13" height="12" viewBox="0 0 13 12"><path d="M2 0v12M5 0v12M8 0v12M11 0v12" stroke="#999"/><path d="M1 4h2M4 7h2M7 3h2M10 8h2" stroke="#666" stroke-width="2"/></svg>Length<span class="chev"></span></div>
  <div class="filter"><svg width="12" height="14" viewBox="0 0 13 14"><rect x="1" y="1" width="8" height="10" fill="none" stroke="#999"/><rect x="4" y="3" width="8" height="10" fill="#eee" stroke="#999"/></svg>Word Count<span class="chev"></span></div>
  <div class="filter"><svg width="15" height="15" viewBox="0 0 15 15"><circle cx="7.5" cy="7.5" r="7" fill="#8a8a8a"/><path d="M4 4c2 0 2 3 4 3s1 4 3 4M3 10c1 0 2-1 3 1" fill="none" stroke="#ddd"/></svg>Language<span class="chev"></span></div>
</div>

<div class="abs listing"><div class="bar"></div></div>

<table class="abs table">
  <thead><tr><th></th><th></th><th></th><th>Price</th></tr></thead>
  <tbody>
    <tr><td class="name">RateHarbor.com</td><td class="cat"><span><svg class="ico"><use href="#i-rocket"/></svg>Business and Finance</span></td><td class="price"><span class="pill">$15,500</span></td><td class="act"><span class="offer">Make Offer</span></td></tr>
    <tr><td class="name">RateHarbor.com</td><td class="cat"><span><svg class="ico"><use href="#i-bank"/></svg>Business and Finance</span></td><td class="price"><span class="pill">$15,500</span></td><td class="act"><span class="offer">Make Offer</span></td></tr>
    <tr><td class="name">RateHarbor.com</td><td class="cat"><span><svg class="ico"><use href="#i-cart"/></svg>Business and Finance</span></td><td class="price"><span class="pill">$15,500</span></td><td class="act"><span class="offer">Make Offer</span></td></tr>
    <tr><td class="name">RateHarbor.com</td><td class="cat"><span><svg class="ico"><use href="#i-rocket"/></svg>Business and Finance</span></td><td class="price"><span class="pill">$15,500</span></td><td class="act"><span class="offer">Make Offer</span></td></tr>
    <tr><td class="name">RateHarbor.com</td><td class="cat"><span><svg class="ico"><use href="#i-cap"/></svg>Business and Finance</span></td><td class="price"><span class="pill">$15,500</span></td><td class="act"><span class="offer">Make Offer</span></td></tr>
    <tr><td class="name">RateHarbor.com</td><td class="cat"><span><svg class="ico"><use href="#i-key"/></svg>Business and Finance</span></td><td class="price"><span class="pill">$15,500</span></td><td class="act"><span class="offer">Make Offer</span></td></tr>
    <tr><td class="name">RateHarbor.com</td><td class="cat"><span><svg class="ico"><use href="#i-rocket"/></svg>Business and Finance</span></td><td class="price"><span class="pill">$15,500</span></td><td class="act"><span class="offer">Make Offer</span></td></tr>
    <tr><td class="name">RateHarbor.com</td><td class="cat"><span><svg class="ico"><use href="#i-cap"/></svg>Business and Finance</span></td><td class="price"><span class="pill">$15,500</span></td><td class="act"><span class="offer">Make Offer</span></td></tr>
    <tr><td class="name">RateHarbor.com</td><td class="cat"><span><svg class="ico"><use href="#i-cart"/></svg>Business and Finance</span></td><td class="price"><span class="pill">$15,500</span></td><td class="act"><span class="offer">Make Offer</span></td></tr>
    <tr><td class="name">RateHarbor.com</td><td class="cat"><span><svg class="ico"><use href="#i-rocket"/></svg>Business and Finance</span></td><td class="price"><span class="pill">$15,500</span></td><td class="act"><span class="offer">Make Offer</span></td></tr>
    <tr><td class="name">RateHarbor.com</td><td class="cat"><span><svg class="ico"><use href="#i-cap"/></svg>Business and Finance</span></td><td class="price"><span class="pill">$15,500</span></td><td class="act"><span class="offer">Make Offer</span></td></tr>
    <tr><td class="name">RateHarbor.com</td><td class="cat"><span><svg class="ico"><use href="#i-pin"/></svg>Business and Finance</span></td><td class="price"><span class="pill">$15,500</span></td><td class="act"><span class="offer">Make Offer</span></td></tr>
    <tr><td class="name">RateHarbor.com</td><td class="cat"><span><svg class="ico"><use href="#i-bank"/></svg>Business and Finance</span></td><td class="price"><span class="pill">$15,500</span></td><td class="act"><span class="offer">Make Offer</span></td></tr>
    <tr><td class="name">RateHarbor.com</td><td class="cat"><span><svg class="ico"><use href="#i-rocket"/></svg>Business and Finance</span></td><td class="price"><span class="pill">$15,500</span></td><td class="act"><span class="offer">Make Offer</span></td></tr>
    <tr><td class="name">RateHarbor.com</td><td class="cat"><span><svg class="ico"><use href="#i-key"/></svg>Business and Finance</span></td><td class="price"><span class="pill">$15,500</span></td><td class="act"><span class="offer">Make Offer</span></td></tr>
    <tr><td class="name">RateHarbor.com</td><td class="cat"><span><svg class="ico"><use href="#i-pin"/></svg>Business and Finance</span></td><td class="price"><span class="pill">$15,500</span></td><td class="act"><span class="offer">Make Offer</span></td></tr>
  </tbody>
</table>

<div class="abs dropdown">
  <div class="abs dd-col" style="left:19px">
    <div class="dd-item"><span class="plus"></span>Automotive</div>
    <div class="dd-item"><span class="plus"></span>Business and Finance</div>
    <div class="dd-item"><span class="plus"></span>Computers and Internet</div>
    <div class="dd-item"><span class="plus"></span>Education</div>
    <div class="dd-item last"><span class="plus"></span>Entertainment</div>
  </div>
  <div class="abs dd-col" style="left:186px">
    <div class="dd-item"><span class="plus"></span>Family</div>
    <div class="dd-item"><span class="plus"></span>Food and Beverage</div>
    <div class="dd-item"><span class="plus"></span>Games</div>
    <div class="dd-item"><span class="plus"></span>Home and Garden</div>
    <div class="dd-item last"><span class="plus"></span>Health and Beauty</div>
  </div>
  <div class="abs dd-col" style="left:353px">
    <div class="dd-item"><span class="plus"></span>Lifestyle</div>
    <div class="dd-item"><span class="plus"></span>Shopping</div>
    <div class="dd-item"><span class="plus"></span>Travel</div>
    <div class="dd-item last"><span class="plus"></span>Sports</div>
  </div>
</div>

<div class="abs pager">
  <span class="wide">Prev</span><span>1</span><span>2</span><span>3</span><span>4</span><span>5</span><span>6</span><span>...</span><span>22</span><span class="wide">Next</span>
</div>

<footer class="abs footer">
  <div class="abs fcol" style="left:130px"><h3>About Us</h3><ul>
    <li>Our Team</li><li>Join our newsletter!</li><li>About Us</li><li>VelraMarkets</li><li>News</li><li>Blog</li><li>FAQ</li><li>Success Stories</li><li>Membership Contract</li><li>Privacy Policy</li></ul></div>
  <div class="abs fcol" style="left:252px"><h3>Buy Domains</h3><ul>
    <li>Premium Domains</li><li>Bargain Domains</li><li>Popular Domains</li><li>Top keywords</li></ul></div>
  <div class="abs fcol" style="left:380px"><h3>Categories</h3><ul>
    <li>Automotive</li><li>Business and Finance</li><li>Computers and Internet</li><li>Education</li><li>Entertainment</li><li>Family</li><li>Food and Beverage</li><li>Games</li></ul></div>
  <div class="abs fcol" style="left:515px"><h3>&nbsp;</h3><ul>
    <li>Home and Garden</li><li>Health and Beauty</li><li>Lifestyle</li><li>Shopping</li><li>Travel</li><li>Privacy Policy</li></ul></div>
  <div class="abs fcol" style="left:637px"><h3>Service</h3><ul>
    <li>Affiliate</li><li>Valuation</li><li>Contact Us</li></ul></div>
  <div class="abs verified"></div>
  <div class="abs cards"><span></span><span></span><span></span><span></span></div>
</footer>
<div class="abs copyright">Copyrights © 2014. Parcelnest. All Rights Reserved.</div>
</body>
</html>
```